Need a professional card design. Marlowe building company specialise in residential and commercial builds. New homes, additions & renovations.
Wanting a card with creativity and professionalism.
Want card that utilises logo.

Back and front.

I have just created a logo, and want to use it on the business card.
Attached a copy of the logo.
Attached is also a current business card which I wish to redesign

please utilise both sides

• Reg# 38095

```html
<!DOCTYPE html>
<html lang="en">
<head>
<meta charset="utf-8">
<title>Marlowe Building Co — Business Card</title>
<link rel="stylesheet" href="https://fonts.googleapis.com/css2?family=Cinzel:wght@500&family=Tinos&family=Open+Sans:wght@400;600&display=swap">
<style>
  :root {
    --page: #d9d4cc;
    --espresso: #2d2421;
    --espresso-deep: #231c1a;
    --gold: #e9a53a;
    --paper: #ffffff;
    --ink: #2b2b2b;
    --rule: #3a3a3a;
  }
  * { box-sizing: border-box; margin: 0; padding: 0; }
  html, body { width: 1200px; height: 1024px; overflow: hidden; }
  body {
    background: var(--page);
    display: flex; flex-direction: column; align-items: center; justify-content: center;
    gap: 36px;
  }
  .card {
    position: relative; width: 800px; height: 457px; overflow: hidden;
    box-shadow: 0 6px 18px rgba(0,0,0,.18);
  }

  /* Front */
  .card--front { background: var(--espresso); }
  .front__rule-top {
    position: absolute; left: 60px; right: 60px; top: 70px; height: 1.5px; background: var(--gold);
  }
  .front__brand {
    position: absolute; left: 0; right: 0; top: 150px; text-align: center;
    font-family: "Cinzel", serif; font-weight: 500; font-size: 58px; letter-spacing: 3px;
    color: var(--gold); line-height: 1;
  }
  .front__brand-mark {
    display: inline-block; width: 18px; height: 18px; background: var(--gold);
    margin-right: 18px; vertical-align: 10px;
  }
  .front__tagline {
    position: absolute; left: 0; right: 0; top: 268px; text-align: center;
    font-family: "Tinos", serif; font-size: 25px; line-height: 1.3; color: var(--gold);
  }
  .front__tagline-rule {
    position: absolute; left: 170px; right: 170px; height: 1.5px; background: var(--gold);
  }
  .front__tagline-rule--a { top: 256px; }
  .front__tagline-rule--b { top: 346px; }
  .front__rule-bottom {
    position: absolute; left: 60px; right: 60px; bottom: 50px; height: 1.5px; background: var(--gold);
  }

  /* Back */
  .card--back { background: var(--paper); }
  .back__brand {
    position: absolute; left: 56px; top: 46px;
    font-family: "Cinzel", serif; font-weight: 500; font-size: 38px; letter-spacing: 2px;
    color: var(--gold); line-height: 1;
  }
  .back__brand-mark {
    display: inline-block; width: 12px; height: 12px; background: var(--gold);
    margin-right: 12px; vertical-align: 7px;
  }
  .back__tagline {
    position: absolute; left: 56px; top: 104px;
    font-family: "Tinos", serif; font-style: italic; font-size: 16px; line-height: 1.35; color: var(--ink);
  }
  .back__divider {
    position: absolute; left: 40px; width: 370px; top: 178px; height: 1px; background: var(--rule);
  }
  .back__contacts {
    position: absolute; left: 56px; top: 200px; list-style: none;
    font-family: "Open Sans", sans-serif; font-size: 17px; color: var(--ink);
  }
  .back__contacts li { display: flex; align-items: center; gap: 12px; height: 30px; }
  .back__contacts svg { width: 16px; height: 16px; fill: var(--gold); flex: none; }
  .back__person {
    position: absolute; right: 70px; top: 196px; text-align: right;
  }
  .back__name {
    font-family: "Cinzel", serif; font-weight: 500; font-size: 30px; letter-spacing: 1.5px; color: var(--ink);
  }
  .back__role {
    margin-top: 6px; font-family: "Open Sans", sans-serif; font-weight: 600; font-size: 18px; color: var(--gold);
  }
  .back__gold-band {
    position: absolute; left: 0; right: 0; bottom: 62px; height: 12px; background: var(--gold);
  }
  .back__dark-band {
    position: absolute; left: 0; right: 0; bottom: 0; height: 62px; background: var(--espresso-deep);
    display: flex; align-items: center; padding-left: 40px;
    font-family: "Open Sans", sans-serif; font-weight: 600; font-size: 17px; color: var(--paper);
  }
</style>
</head>
<body>
  <section class="card card--front" aria-label="Card front">
    <div class="front__rule-top"></div>
    <div class="front__brand"><span class="front__brand-mark"></span>Marlowe Building Co</div>
    <div class="front__tagline-rule front__tagline-rule--a"></div>
    <p class="front__tagline">New Homes - Additions &amp; Renovations<br>Domestic &amp; Commercial Builders</p>
    <div class="front__tagline-rule front__tagline-rule--b"></div>
    <div class="front__rule-bottom"></div>
  </section>

  <section class="card card--back" aria-label="Card back">
    <div class="back__brand"><span class="back__brand-mark"></span>Marlowe Building Co</div>
    <p class="back__tagline">New Homes - Additions &amp; Renovations<br>Domestic &amp; Commercial Builders</p>
    <div class="back__divider"></div>
    <ul class="back__contacts">
      <li><svg viewBox="0 0 16 16" aria-hidden="true"><path d="M3.5 1l2.5 3-1.5 2c.8 2 2.5 3.7 4.5 4.5l2-1.5 3 2.5-1.5 2.5C7.5 15 1 8.5 1 2.5z"/></svg>08 6142 5580</li>
      <li><svg viewBox="0 0 16 16" aria-hidden="true"><path d="M2 5h12v8H2zM4 2h8v3H4zM5 9h6v2H5z"/></svg>08 6142 5580</li>
      <li><svg viewBox="0 0 16 16" aria-hidden="true"><path d="M4 1h8a1 1 0 0 1 1 1v12a1 1 0 0 1-1 1H4a1 1 0 0 1-1-1V2a1 1 0 0 1 1-1zm1 2v9h6V3zm3 10a.8.8 0 1 0 0 1.6.8.8 0 0 0 0-1.6z"/></svg>0412 845 093</li>
      <li><svg viewBox="0 0 16 16" aria-hidden="true"><path d="M1 3h14v10H1zm1.5 1.2v.4L8 8.5l5.5-3.9v-.4z"/></svg>marlowebuildingco@mailbox.com</li>
    </ul>
    <div class="back__person">
      <p class="back__name">Pavel Dorsan</p>
      <p class="back__role">Director</p>
    </div>
    <div class="back__gold-band"></div>
    <div class="back__dark-band">Reg. No. 38095</div>
  </section>
</body>
</html>
```